DLW Flyer 2022

Need a flyer/Brochure it it an information piece on or company to give to clients during Sales call. I have started something in Canva but would like it more professional designed. We we are a Fire & Security company.
we do alot of cloud based systems. New system intercoms, Camera systems, Card Access and fire alarm systems

```html
<!DOCTYPE html>
<html lang="en">
<head>
<meta charset="utf-8">
<title>DLW Fire &amp; Security Brochure</title>
<link href="https://fonts.googleapis.com/css2?family=Poppins:ital,wght@0,300;0,400;0,500;0,700;0,800;1,400&display=swap" rel="stylesheet">
<style>
:root{
  --bg:#e4e4e4;
  --red:#d7262f;
  --red-soft:#e4434b;
  --white:#ffffff;
  --paper:#f3f3f3;
  --grey-panel:#e9e9e9;
  --ink:#2b2b2b;
  --dark-bar:#3a3a3a;
}
*{box-sizing:border-box;margin:0;padding:0}
html,body{width:1200px;height:857px;overflow:hidden;background:var(--bg);font-family:'Poppins',sans-serif;color:var(--ink)}
.canvas{position:relative;width:1200px;height:857px}
.spread{position:absolute;left:70px;top:140px;width:780px;height:580px;display:flex;box-shadow:0 12px 30px rgba(0,0,0,.15)}
.panel{position:relative;width:260px;height:580px;overflow:hidden}

/* panel 1 */
.panel-why{background:var(--paper)}
.photo-operator{position:absolute;left:0;top:0;width:260px;height:290px;background:linear-gradient(160deg,#e9545c 0%,#c0393f 45%,#6e4a4c 100%)}
.hero-title{position:absolute;left:22px;top:170px;color:var(--white);font-size:19px;line-height:1.15;font-weight:400}
.dark-bar{position:absolute;left:0;top:290px;width:150px;height:6px;background:var(--dark-bar)}
.why-heading{position:absolute;left:22px;top:340px}
.why-heading .small{font-size:18px;font-weight:400;display:block}
.why-heading .big{font-size:30px;font-weight:800;color:var(--red);line-height:1}
.why-sub{position:absolute;left:22px;top:405px;font-size:10.5px}
.quote-name{position:absolute;left:22px;top:440px;font-size:15px;font-weight:500}
.quote-text{position:absolute;left:22px;top:465px;font-size:10.5px;line-height:1.4;width:200px}
.band-bottom{position:absolute;left:0;bottom:0;width:100%;height:14px;background:var(--red)}

/* panel 2 */
.panel-services{background:var(--red);color:var(--white);text-align:center}
.services-title{margin-top:36px;font-size:14px;font-weight:400;letter-spacing:.5px}
.service{margin:18px auto 0;width:210px}
.service svg{display:block;margin:0 auto 4px}
.service h3{font-size:12.5px;font-weight:800;font-style:italic}
.service p{font-size:9px;line-height:1.45;font-weight:300}

/* panel 3 */
.panel-about{background:var(--grey-panel)}
.band-top{position:absolute;left:0;top:0;width:100%;height:12px;background:var(--red)}
.about-title{position:absolute;left:22px;top:48px;font-size:20px;font-weight:400;font-style:italic}
.about-text{position:absolute;left:22px;top:86px;width:215px;font-size:9.2px;line-height:1.55;font-style:italic}
.red-rule{position:absolute;left:60px;top:272px;width:170px;height:5px;background:var(--red)}
.photo-cameras{position:absolute;left:0;top:300px;width:260px;height:220px;background:linear-gradient(180deg,#9c9c9c 0%,#cfcfcf 55%,#f1f1f1 100%)}

/* cover */
.cover{position:absolute;left:900px;top:140px;width:240px;height:580px;background:var(--white);overflow:hidden;box-shadow:0 12px 30px rgba(0,0,0,.15)}
.cover .band-top{height:14px}
.brand{position:absolute;left:0;top:84px;width:100%;text-align:center}
.brand-name{font-size:30px;font-weight:800;color:var(--red);display:flex;align-items:center;justify-content:center;gap:8px}
.brand-mark{width:12px;height:12px;background:var(--red)}
.brand-line{font-size:10px;font-weight:800;color:var(--red);letter-spacing:.5px}
.brand-url{margin-top:10px;font-size:11px;letter-spacing:1.5px}
.cover-art{position:absolute;left:0;top:170px}
.tagline{position:absolute;left:22px;top:268px;color:var(--white)}
.tagline .main{font-size:28px;font-weight:800;display:block;line-height:1}
.tagline .sub{font-size:17px;font-weight:400;padding-left:14px}
.illus-lock{position:absolute;left:0;top:340px;width:240px;height:240px;background:radial-gradient(circle at 50% 40%,#e6e6e6 0%,#b9b9b9 60%,#9a9a9a 100%)}
</style>
</head>
<body>
<div class="canvas">
  <section class="spread">
    <article class="panel panel-why">
      <div class="photo-operator" role="img" aria-label="Red-tinted photo of a technician operating a fire alarm control panel"></div>
      <h2 class="hero-title">Fire Alarm and<br>Emergency<br>Communications<br>Systems</h2>
      <div class="dark-bar"></div>
      <h2 class="why-heading"><span class="small">Why</span><span class="big">Choose us?</span></h2>
      <p class="why-sub">We are here to make your job easier.</p>
      <p class="quote-name">– Anonymous</p>
      <p class="quote-text">Man with hole in pocket feel cocky all day</p>
      <div class="band-bottom"></div>
    </article>

    <article class="panel panel-services">
      <h2 class="services-title">Company Services</h2>
      <div class="service">
        <svg width="40" height="32" viewBox="0 0 40 32" fill="none" stroke="#fff" stroke-width="1.5"><path d="M10 22h22a6 6 0 0 0 0-12 9 9 0 0 0-17-2 7 7 0 0 0-5 14z"/><path d="M16 22v5M20 22v7M24 22v5"/></svg>
        <h3>Cloud Services</h3>
        <p>Providing a secure, convenient, and affordable way to manage your systems on the go, from any device. No more costly hardware or software to maintain.</p>
      </div>
      <div class="service">
        <svg width="40" height="32" viewBox="0 0 40 32" fill="none" stroke="#fff" stroke-width="1.5"><rect x="6" y="3" width="28" height="20" rx="3"/><circle cx="14" cy="11" r="3"/><path d="M22 9h8M22 14h8M10 18h20"/></svg>
        <h3>Intercom &amp; Access</h3>
        <p>Let us design an access system for your building. Local, PC or cloud programming. Full Featured or Basic</p>
      </div>
      <div class="service">
        <svg width="40" height="32" viewBox="0 0 40 32" fill="none" stroke="#fff" stroke-width="1.5"><path d="M6 16 20 4l14 12M10 13v16h20V13"/><rect x="17" y="17" width="6" height="8"/></svg>
        <h3>Fire Alarm</h3>
        <p>Testing, Maintenance and Installation<br>Central Station Monitoring<br>24 hr. Service Mass. License 25C</p>
      </div>
      <div class="service">
        <svg width="40" height="32" viewBox="0 0 40 32" fill="none" stroke="#fff" stroke-width="1.5"><rect x="6" y="8" width="22" height="12" rx="2"/><circle cx="17" cy="14" r="3"/><path d="M28 12l6-3v10l-6-3M12 20v8"/></svg>
        <h3>Camera Systems</h3>
        <p>Camera's system designed to meet you needs. view for anywhere</p>
      </div>
    </article>

    <article class="panel panel-about">
      <div class="band-top"></div>
      <h2 class="about-title">About us</h2>
      <p class="about-text">DLW has been serving the Greater Boston and surrounding areas Fire and Security systems since 1988. It is our privilege to provide superior service with highly trained and experienced technicians. Our technicians surpass expectations with their product knowledge, job performance, and pride in workmanship to deliver dependable systems that fit any situation</p>
      <div class="red-rule"></div>
      <div class="photo-cameras" role="img" aria-label="Grey photo of dome and PTZ security cameras in front of a video wall"></div>
    </article>
  </section>

  <section class="cover">
    <div class="band-top"></div>
    <div class="brand">
      <div class="brand-name"><span class="brand-mark"></span>DLW</div>
      <div class="brand-line">FIRE &amp; SECURITY SYSTEMS</div>
      <div class="brand-url">www.dlwsecurity.com</div>
    </div>
    <svg class="cover-art" width="240" height="170" viewBox="0 0 240 170"><polygon points="0,10 240,70 240,170 0,170" fill="#d7262f"/></svg>
    <div class="illus-lock" role="img" aria-label="Grey 3D illustration of an open padlock among floating spheres and circuit lines"></div>
    <h2 class="tagline"><span class="main">Unlocking</span><span class="sub">The Furture</span></h2>
  </section>
</div>
</body>
</html>
```